Culture consulting company business card - first step

I created a new venture called The Harbor Keystone. It's focused on improving the organizational culture of companies and I have a logo, tag line and other basic info but I need an overall design theme I'll carry through to letterhead, marketing literature, direct mail post cards, whitepapers, video intros and my web site. The business card design is a trial to develop the theme and more projects will hopefully follow for the winner! This business will grow fast and I need a great design theme to leverage.

Target Market(s)

Target Market is both for profit and non profit businesses. Special emphasis on consulting companies, foundations and venture capital firms

Industry/Entity Type

Marketing

Requirements
Must have
• The Harbor Keystone Logo
Name (Ned Wastrom)
Phone (313-574-6190)
E-mail (Ned@The-Harbor-Keystone.com)
Web Site (www.The-Harbor-Keystone.com)
Tag line in some way: "Culture Shift with Focus and Momentum"
- Clarity and Speed should be in red with speed potentially in italics. The other words in black.

Front and back of card design - front has info above
Back should have The Harbor Keystone logo and a list of areas we focus on with the red check mark image next to each. The areas are: Performance Improvement, Organizational Excellence, Strategic Alignment, Team Effectiveness, Onboarding, Leadership Development & Coaching

Overall key colors are in the logo (red & black)

NEED DESIGN FORMAT in a PHOTOSHOP / PSD FILE. Photoshop template from printer is attached. Needs to follow the diminsions / guidelines.
Nice to have
• Potentially "road" picture if it fits with a great theme
Should not have
• Needs to be veryprofessional looking but it's fine to come across as very innovative, interesting or unique. Need clear design / fonts and color theme I can carry through to other print and web formats.

```html
<!DOCTYPE html>
<html lang="en">
<head>
<meta charset="utf-8">
<title>The Harbor Keystone — Business Card</title>
<link href="https://fonts.googleapis.com/css2?family=Questrial&display=swap" rel="stylesheet">
<style>
  :root {
    --stage: #d6d6d8;
    --red: #d0101e;
    --red-deep: #7a0a10;
    --black: #0d0d0d;
    --charcoal: #2c2c2e;
    --steel: #9a9a9c;
    --silver: #e9e9ea;
    --white: #ffffff;
    --ink: #111111;
  }
  * { box-sizing: border-box; margin: 0; padding: 0; }
  html, body { width: 1200px; height: 765px; overflow: hidden; }
  body {
    background: var(--stage);
    font-family: "Questrial", "Century Gothic", sans-serif;
    position: relative;
  }
  .card {
    position: absolute;
    top: 302px;
    width: 575px;
    height: 344px;
    border-radius: 30px;
    overflow: hidden;
    box-shadow: 0 6px 14px rgba(0,0,0,.25);
  }
  .card--front { left: 17px; }
  .card--back { left: 608px; }
  .card__art { position: absolute; inset: 0; width: 100%; height: 100%; }

  /* front */
  .tagline {
    position: absolute; left: 50px; top: 40px;
    font-size: 13px; color: var(--ink); letter-spacing: .1px; white-space: nowrap;
  }
  .tagline__accent { color: var(--red); font-style: italic; }
  .holder-name {
    position: absolute; left: 214px; top: 112px;
    font-size: 37px; font-weight: 400; color: var(--ink); letter-spacing: .3px;
  }
  .contact { position: absolute; left: 226px; top: 218px; list-style: none; }
  .contact__item {
    display: flex; align-items: center; gap: 8px;
    color: var(--white); font-size: 17px; height: 25px; margin-bottom: 2px;
    white-space: nowrap;
  }
  .contact__item--phone { font-size: 24px; height: 30px; }
  .contact__icon { width: 19px; height: 19px; flex: none; }
  .front-brand {
    position: absolute; left: 44px; top: 254px; width: 100px;
    text-align: center; font-size: 12px; line-height: 1.2;
    color: var(--red); text-transform: uppercase;
  }

  /* back */
  .back-brand {
    position: absolute; left: 160px; top: 86px; width: 360px;
    text-align: center; color: var(--red); text-transform: uppercase;
    line-height: 1.05;
  }
  .back-brand__small { display: block; font-size: 26px; }
  .back-brand__large { display: block; font-size: 40px; }
  .focus-list {
    position: absolute; left: 48px; top: 240px;
    display: grid; grid-template-columns: 195px 260px;
    row-gap: 3px; list-style: none;
  }
  .focus-list__item {
    display: flex; align-items: center; gap: 5px;
    color: var(--white); font-size: 13.5px; height: 18px; white-space: nowrap;
  }
  .focus-list__tick { width: 16px; height: 18px; flex: none; }
</style>
</head>
<body>

<section class="card card--front" aria-label="Card front">
  <svg class="card__art" viewBox="0 0 575 344" aria-hidden="true">
    <defs>
      <linearGradient id="frontPhoto" x1="0" y1="0" x2="1" y2="1">
        <stop offset="0" stop-color="#b3121b"/>
        <stop offset=".45" stop-color="#6d0a0f"/>
        <stop offset="1" stop-color="#c9c9cb"/>
      </linearGradient>
      <linearGradient id="topBand" x1="0" y1="0" x2="1" y2="0">
        <stop offset="0" stop-color="#ffffff"/>
        <stop offset=".7" stop-color="#f2f2f2"/>
        <stop offset="1" stop-color="#cfcfd0"/>
      </linearGradient>
      <linearGradient id="darkPanel" x1="0" y1="0" x2="1" y2="0">
        <stop offset="0" stop-color="#0a0a0a"/>
        <stop offset=".55" stop-color="#2a2a2c"/>
        <stop offset="1" stop-color="#6b6b6d"/>
      </linearGradient>
      <linearGradient id="namePlate" x1="0" y1="0" x2="0" y2="1">
        <stop offset="0" stop-color="#ffffff"/>
        <stop offset="1" stop-color="#d8d8da"/>
      </linearGradient>
      <linearGradient id="lowerRoad" x1="0" y1="0" x2="1" y2="1">
        <stop offset="0" stop-color="#e4e4e5"/>
        <stop offset="1" stop-color="#a9a9ab"/>
      </linearGradient>
    </defs>
    <rect width="575" height="344" fill="url(#frontPhoto)"/>
    <g role="img" aria-label="Red-toned photograph of a bridge and coastal road">
      <rect x="0" y="60" width="575" height="284" fill="url(#frontPhoto)"/>
    </g>
    <path d="M0 230 C60 250 80 300 60 344 L0 344 Z" fill="url(#lowerRoad)" opacity=".9"/>
    <path d="M0 0 H400 C370 20 360 55 330 62 H0 Z" fill="url(#topBand)"/>
    <path d="M0 62 H330 C355 58 372 30 400 0 H420 C390 35 372 70 335 72 H0 Z" fill="#9a0d14"/>
    <path d="M135 150 Q150 138 175 138 H520 Q545 138 545 162 V296 Q545 320 520 320 H150 Q125 320 118 300 L100 232 Z" fill="url(#darkPanel)"/>
    <path d="M213 84 H515 Q530 84 525 98 L505 170 Q500 184 485 184 H215 Q200 184 200 170 V98 Q200 84 213 84 Z" fill="url(#namePlate)" stroke="#bdbdbf" stroke-width="1.5"/>
  </svg>

  <p class="tagline">Culture Shift with <span class="tagline__accent">Focus and Momentum</span></p>
  <h1 class="holder-name">Ned Wastrom</h1>

  <ul class="contact">
    <li class="contact__item contact__item--phone">
      <svg class="contact__icon" viewBox="0 0 20 20" aria-hidden="true"><rect width="20" height="20" rx="3" fill="var(--red)"/><path d="M6 4 L8.5 4 L9.5 7 L8 8.3 Q9.5 11.5 12 12.5 L13.3 11 L16 12 V14.5 Q15 16 13 16 Q6 14 4.5 7 Q4.5 5 6 4 Z" fill="#fff"/></svg>
      <span>313-574-6190</span>
    </li>
    <li class="contact__item">
      <svg class="contact__icon" viewBox="0 0 20 20" aria-hidden="true"><rect width="20" height="20" rx="3" fill="var(--red)"/><rect x="4" y="6" width="12" height="8.5" fill="none" stroke="#fff" stroke-width="1.5"/><path d="M4 6 L10 11 L16 6" fill="none" stroke="#fff" stroke-width="1.5"/></svg>
      <span>Ned@The-Harbor-Keystone.com</span>
    </li>
    <li class="contact__item">
      <svg class="contact__icon" viewBox="0 0 20 20" aria-hidden="true"><rect width="20" height="20" rx="3" fill="var(--red)"/><circle cx="9" cy="9" r="4" fill="none" stroke="#fff" stroke-width="1.8"/><path d="M12 12 L15.5 15.5" stroke="#fff" stroke-width="2"/></svg>
      <span>www.The-Harbor-Keystone.com</span>
    </li>
  </ul>

  <p class="front-brand">The Harbor Keystone</p>
</section>

<section class="card card--back" aria-label="Card back">
  <svg class="card__art" viewBox="0 0 575 344" aria-hidden="true">
    <defs>
      <linearGradient id="backPhoto" x1="0" y1="0" x2="0" y2="1">
        <stop offset="0" stop-color="#dcdadb"/>
        <stop offset=".6" stop-color="#a8a5a6"/>
        <stop offset="1" stop-color="#7a7778"/>
      </linearGradient>
      <linearGradient id="backLower" x1="0" y1="0" x2="1" y2="0">
        <stop offset="0" stop-color="#1a0204"/>
        <stop offset=".45" stop-color="#b2101a"/>
        <stop offset="1" stop-color="#1a0204"/>
      </linearGradient>
      <linearGradient id="logoPlate" x1="0" y1="0" x2="1" y2="0">
        <stop offset="0" stop-color="#111"/>
        <stop offset=".12" stop-color="#c9c9cb"/>
        <stop offset=".35" stop-color="#ffffff"/>
        <stop offset="1" stop-color="#e2e2e3"/>
      </linearGradient>
    </defs>
    <g role="img" aria-label="Muted grey photograph of a bridge and road along the coast">
      <rect width="575" height="190" fill="url(#backPhoto)"/>
    </g>
    <path d="M0 170 Q280 150 575 175 V344 H0 Z" fill="url(#backLower)"/>
    <path d="M125 71 H520 Q535 71 535 86 V212 Q535 229 518 229 H240 Q210 229 195 205 L118 88 Q110 71 125 71 Z" fill="url(#logoPlate)" stroke="#ffffff" stroke-width="2"/>
  </svg>

  <p class="back-brand">
    <span class="back-brand__small">The</span>
    <span class="back-brand__large">Harbor</span>
    <span class="back-brand__large">Keystone</span>
  </p>

  <ul class="focus-list">
    <li class="focus-list__item"><svg class="focus-list__tick" viewBox="0 0 16 18" aria-hidden="true"><path d="M1 10 L4 8 L6.5 13 L13 1 L15.5 2 L7 17 Z" fill="var(--red)"/></svg>Performance Improvement</li>
    <li class="focus-list__item"><svg class="focus-list__tick" viewBox="0 0 16 18" aria-hidden="true"><path d="M1 10 L4 8 L6.5 13 L13 1 L15.5 2 L7 17 Z" fill="var(--red)"/></svg>Organizational Excellence</li>
    <li class="focus-list__item"><svg class="focus-list__tick" viewBox="0 0 16 18" aria-hidden="true"><path d="M1 10 L4 8 L6.5 13 L13 1 L15.5 2 L7 17 Z" fill="var(--red)"/></svg>Strategic Alignment</li>
    <li class="focus-list__item"><svg class="focus-list__tick" viewBox="0 0 16 18" aria-hidden="true"><path d="M1 10 L4 8 L6.5 13 L13 1 L15.5 2 L7 17 Z" fill="var(--red)"/></svg>Team Effectiveness</li>
    <li class="focus-list__item"><svg class="focus-list__tick" viewBox="0 0 16 18" aria-hidden="true"><path d="M1 10 L4 8 L6.5 13 L13 1 L15.5 2 L7 17 Z" fill="var(--red)"/></svg>Onboarding</li>
    <li class="focus-list__item"><svg class="focus-list__tick" viewBox="0 0 16 18" aria-hidden="true"><path d="M1 10 L4 8 L6.5 13 L13 1 L15.5 2 L7 17 Z" fill="var(--red)"/></svg>Leadership Development &amp; Coaching</li>
  </ul>
</section>

</body>
</html>
```